Professional Label needed for Meadowpaw Snack Co

I make 100% organic dog treats. Wheat and gluten free.

I will be packaging them in a window kraft bag. I need a nicely designed label to place on each bag. The name of my company is The Meadowpaw Snack Company. All ingredients are organic and no preservatives are used. They are a healthy alternative to "assembly line" treats made by large companies.

Target Market(s)

Dog Owners

Industry/Entity Type

Pet

Font styles to use
Serif

Colors
00a990

Requirements
Must have
• can use a dog paw - see attached files. Dog themed, 100%
• Organic Dog Treats.
• No preservatives, nothing artificial, no corn, wheat or soy, made in Texas, USA with 100% organic ingredients. Non GMO
• Must have "dog treat" somewhere.
• "The Meadowpaw Snack Co." font size needs to be bigger than anything else.
Nice to have
• I like teal and brown
• I'm open to anything really as long as its dog themed

```html
<!DOCTYPE html>
<html lang="en">
<head>
<meta charset="utf-8">
<title>The Meadowpaw Snack Co. – Dog Treats Label</title>
<link rel="stylesheet" href="https://fonts.googleapis.com/css2?family=Arvo:wght@400;700&display=swap">
<style>
  :root {
    --teal: #14a08c;
    --teal-deep: #0d7f70;
    --kraft: #c7a57c;
    --kraft-dark: #a9875f;
    --brown: #4a3322;
    --cream: #f3e6cf;
    --white: #ffffff;
    --stage: #eeeeee;
  }
  html, body {
    margin: 0;
    padding: 0;
    width: 750px;
    height: 1200px;
    overflow: hidden;
    background: var(--stage);
  }
  .canvas {
    position: relative;
    width: 750px;
    height: 1200px;
  }
  .label {
    position: absolute;
    left: 75px;
    top: 300px;
    width: 600px;
    height: 600px;
  }
  .label svg {
    display: block;
    width: 600px;
    height: 600px;
  }
  .brand-arc {
    font-family: "Arvo", Georgia, serif;
    font-weight: 700;
    font-size: 40px;
    letter-spacing: 2px;
    fill: var(--brown);
  }
  .ribbon-percent {
    font-family: "Arvo", Georgia, serif;
    font-weight: 700;
    font-size: 28px;
    fill: var(--brown);
  }
  .ribbon-claim {
    font-family: "Arvo", Georgia, serif;
    font-weight: 400;
    font-size: 20px;
    fill: var(--brown);
  }
  .product-name {
    font-family: "Arvo", Georgia, serif;
    font-weight: 700;
    font-size: 20px;
    letter-spacing: 1px;
    fill: var(--white);
  }
  .origin {
    font-family: "Arvo", Georgia, serif;
    font-weight: 700;
    font-size: 16px;
    letter-spacing: 0.5px;
    fill: var(--brown);
  }
</style>
</head>
<body>
<main class="canvas">
  <section class="label" aria-label="The Meadowpaw Snack Co. dog treats label">
    <svg viewBox="0 0 600 600" xmlns="http://www.w3.org/2000/svg">
      <defs>
        <path id="brand-curve" d="M 87.5 357 A 220 220 0 1 1 512.5 357"/>
        <radialGradient id="mascot-fill" cx="50%" cy="45%" r="60%">
          <stop offset="0%" stop-color="#e9d3ad"/>
          <stop offset="100%" stop-color="#c79a68"/>
        </radialGradient>
      </defs>

      <!-- label frame -->
      <rect class="label-frame" x="0" y="0" width="600" height="600" fill="var(--teal)"/>
      <rect class="label-ground" x="16" y="16" width="568" height="568" fill="var(--kraft)"/>
      <rect class="label-inner-line" x="26" y="26" width="548" height="548" fill="none" stroke="var(--white)" stroke-width="2"/>

      <!-- brand name -->
      <text class="brand-arc"><textPath href="#brand-curve" startOffset="50%" text-anchor="middle">THE MEADOWPAW SNACK CO.</textPath></text>

      <!-- centre medallion -->
      <circle class="medallion-ring" cx="300" cy="300" r="158" fill="var(--cream)"/>
      <circle class="medallion" cx="300" cy="300" r="150" fill="var(--teal)"/>
      <circle class="medallion-line" cx="300" cy="300" r="140" fill="none" stroke="var(--white)" stroke-width="2"/>
      <ellipse class="mascot" cx="300" cy="245" rx="105" ry="80" fill="url(#mascot-fill)" role="img" aria-label="Illustration of a happy dog holding a bone"/>

      <!-- cream ribbon -->
      <path class="ribbon-tail" d="M 70 340 L 40 395 L 80 392 L 92 420 L 120 370 Z" fill="var(--kraft-dark)"/>
      <path class="ribbon-tail" d="M 530 340 L 560 395 L 520 392 L 508 420 L 480 370 Z" fill="var(--kraft-dark)"/>
      <path class="ribbon" d="M 90 320 Q 300 370 510 320 L 510 390 Q 300 440 90 390 Z" fill="var(--cream)" stroke="var(--brown)" stroke-width="2"/>
      <text class="ribbon-percent" x="300" y="372" text-anchor="middle">100%</text>
      <text class="ribbon-claim" x="300" y="400" text-anchor="middle">organic ingredients</text>

      <!-- teal ribbon -->
      <path class="product-band" d="M 190 428 Q 300 450 410 428 L 410 464 Q 300 486 190 464 Z" fill="var(--teal-deep)" stroke="var(--white)" stroke-width="1.5"/>
      <text class="product-name" x="300" y="462" text-anchor="middle">DOG TREATS</text>

      <!-- footer -->
      <text class="origin" x="42" y="560">MADE IN TEXAS, USA</text>
      <g class="claim-badges" fill="var(--kraft-dark)" stroke="var(--white)" stroke-width="2.5">
        <circle cx="410" cy="545" r="24"/>
        <circle cx="475" cy="545" r="24"/>
        <circle cx="540" cy="545" r="24"/>
      </g>
    </svg>
  </section>
</main>
</body>
</html>
```